Home Services (heating, cooling, electrical, plumbing) postcard design

We are looking for postcards to way to send a brief written message to our clients. Most often these will be used by the sales team but there will be opportunity for our techs to reach out to their clients as well.
We don't want them to be sales-y so if the logo, name, or taglines are used we prefer it to be more subtle.
It also doesn't need to match our website design as we are looking for a more casual feel. Something nostalgic/retro/vintage might be fun.

About us: (PLEASE DO NOT USE ANY OF THE FOLLOWING PHRASING ON THE DESIGN, this information is just to give you an idea of who we are)
- a service company that focuses on heating, cooling, electrical and plumbing service and retrofit (residential and commercial)
- family owned
- based in Warman which is a smaller city in rural Saskatchewan
- we have used the tagline "ensuring your comfort, safety and health since 2009"
- values: gratitude, stewardship, teamwork, lifelong learning, communication, quality, service
- we are professional but not stuffy, we have a fun team
- we like to inform and educate our clients

Target Market(s)

clients that we have already engaged with, we are often reaching out to say thanks (for referrals, or for the opportunity to serve them)

Industry/Entity Type

HVAC (heating, ventilation, ac), electrical, plumbing

Requirements
Must have
• Enough room on the back of postcard for mailing address and larger blank space for a message.
Nice to have
• Original designs or artwork (try to avoid stock photos), vintage feel
Should not have
• prefer not to be sales-y or promotional, it's not meant to be about us, any use of BrelloVane logo or information should be subtle

```html
<!DOCTYPE html>
<html lang="en">
<head>
<meta charset="utf-8">
<title>BrelloVane Thank-You Postcard</title>
<link rel="stylesheet" href="https://fonts.googleapis.com/css2?family=Montserrat:wght@300;400;600;700;800;900&display=swap">
<style>
  :root{
    --blue:#1f74bd;
    --orange:#f26322;
    --ink:#1b1b1b;
    --grey:#58595b;
    --paper:#ffffff;
    --page:#eeeeee;
    --rule:#bdbdbd;
    --stamp:#e6e6e6;
    --write-line:rgba(255,255,255,.55);
  }
  *{box-sizing:border-box;margin:0;padding:0}
  html,body{width:783px;height:1200px;overflow:hidden;background:var(--page);font-family:"Montserrat",sans-serif}
  .postcard{position:absolute;left:26px;width:730px;height:486px;background:var(--paper);overflow:hidden;box-shadow:0 3px 8px rgba(0,0,0,.22)}
  .postcard--front{top:60px}
  .postcard--back{top:620px}
  .postcard svg.art{position:absolute;inset:0}
  .abs{position:absolute;white-space:nowrap}
  .defs{position:absolute;width:0;height:0}

  .brand{display:flex;align-items:center;gap:6px}
  .brand__dot{width:12px;height:12px;border-radius:50%;background:var(--orange)}
  .brand__name{font-weight:800;color:var(--blue);letter-spacing:-.5px}
  .brand__services{font-size:10px;font-weight:600;color:var(--ink)}

  .headline__top{font-size:35px;font-weight:900;color:var(--blue);letter-spacing:-.5px;line-height:1}
  .headline__main{font-size:62px;font-weight:900;color:var(--orange);letter-spacing:-1px;line-height:1}
  .headline__sub{font-size:20px;font-weight:900;color:var(--ink);letter-spacing:-.4px}
  .headline__sub span{font-weight:300}

  .values__title{font-size:19px;font-weight:800;color:var(--blue)}
  .values__list{display:grid;grid-template-columns:183px auto;row-gap:8px}
  .values__item{display:flex;align-items:center;gap:7px;font-size:14.5px;font-weight:700;color:var(--ink)}
  .values__item svg{flex:none}

  .contact{color:#fff}
  .contact__row{display:flex;align-items:center;gap:9px}
  .contact__phone{font-size:25px;font-weight:800}
  .contact__web{font-size:16px;font-weight:700}

  .note__title{font-size:21px;font-weight:800;color:#fff}
  .note__title span{color:var(--orange)}
  .follow{font-size:11px;font-weight:700;color:#fff}
  .social{display:flex;gap:8px}
  .social i{display:block;width:20px;height:20px;background:var(--blue)}
</style>
</head>
<body>

<svg class="defs" aria-hidden="true">
  <symbol id="tick" viewBox="0 0 14 14"><circle cx="7" cy="7" r="7" fill="#f26322"/><path d="M3.8 7.2l2.2 2.2 4.2-4.4" stroke="#fff" stroke-width="1.8" fill="none"/></symbol>
  <symbol id="phone" viewBox="0 0 24 24"><path d="M6.6 10.8a15 15 0 006.6 6.6l2.2-2.2a1 1 0 011-.25 11.4 11.4 0 003.6.6 1 1 0 011 1V20a1 1 0 01-1 1A17 17 0 013 4a1 1 0 011-1h3.5a1 1 0 011 1c0 1.25.2 2.45.6 3.6a1 1 0 01-.25 1z" fill="#f26322"/></symbol>
  <symbol id="globe" viewBox="0 0 20 20"><circle cx="10" cy="10" r="8" fill="none" stroke="#f26322" stroke-width="2"/><ellipse cx="10" cy="10" rx="3.5" ry="8" fill="none" stroke="#f26322" stroke-width="1.6"/><line x1="2" y1="10" x2="18" y2="10" stroke="#f26322" stroke-width="1.6"/></symbol>
</svg>

<!-- FRONT -->
<section class="postcard postcard--front">
  <svg class="art" width="730" height="486" viewBox="0 0 730 486">
    <defs>
      <linearGradient id="photoFront" x1="0" y1="0" x2="1" y2="1">
        <stop offset="0" stop-color="#b9d4ee"/>
        <stop offset=".45" stop-color="#8d96a0"/>
        <stop offset="1" stop-color="#4a4c50"/>
      </linearGradient>
      <linearGradient id="blueTri" x1="0" y1="0" x2="0" y2="1">
        <stop offset="0" stop-color="#3a8fd6"/>
        <stop offset="1" stop-color="#1f74bd"/>
      </linearGradient>
      <linearGradient id="fireTri" x1="0" y1="0" x2="0" y2="1">
        <stop offset="0" stop-color="#f7b51b"/>
        <stop offset="1" stop-color="#ee3a1f"/>
      </linearGradient>
    </defs>
    <polygon role="img" aria-label="Photo of a technician in a hard hat servicing rooftop air conditioning units" points="312,0 730,0 730,486 360,486 462,292" fill="url(#photoFront)"/>
    <polygon points="364,486 456,272 590,486" fill="url(#blueTri)" stroke="#fff" stroke-width="5" stroke-linejoin="round" opacity=".92"/>
    <polygon points="734,262 602,486 734,486" fill="url(#fireTri)" stroke="#fff" stroke-width="5" opacity=".92"/>
    <polygon points="0,398 400,398 361,486 0,486" fill="var(--grey)"/>
    <line x1="34" y1="243" x2="353" y2="243" stroke="var(--rule)" stroke-width="1.2"/>
    <line x1="80" y1="243" x2="137" y2="243" stroke="var(--blue)" stroke-width="4" stroke-linecap="round"/>
  </svg>

  <div class="abs brand" style="left:34px;top:30px">
    <i class="brand__dot"></i><span class="brand__name" style="font-size:26px">BrelloVane</span>
  </div>
  <div class="abs brand__services" style="left:34px;top:66px">Heating • Cooling • Electrical • Plumbing</div>

  <div class="abs headline__top" style="left:34px;top:108px">A LITTLE NOTE OF</div>
  <div class="abs headline__main" style="left:32px;top:144px">THANKS</div>
  <div class="abs headline__sub" style="left:36px;top:206px">FROM OUR CREW <span>TO YOUR HOME</span></div>

  <div class="abs values__title" style="left:36px;top:255px">WHAT WE VALUE</div>
  <div class="abs values__list" style="left:36px;top:289px">
    <div class="values__item"><svg width="14" height="14"><use href="#tick"/></svg>Being thankful</div>
    <div class="values__item"><svg width="14" height="14"><use href="#tick"/></svg>Talking openly</div>
    <div class="values__item"><svg width="14" height="14"><use href="#tick"/></svg>Caring for things</div>
    <div class="values__item"><svg width="14" height="14"><use href="#tick"/></svg>Doing it right</div>
    <div class="values__item"><svg width="14" height="14"><use href="#tick"/></svg>Working together</div>
    <div class="values__item"><svg width="14" height="14"><use href="#tick"/></svg>Showing up</div>
    <div class="values__item"><svg width="14" height="14"><use href="#tick"/></svg>Always learning</div>
  </div>

  <div class="abs contact" style="left:36px;top:408px">
    <div class="contact__row"><svg width="20" height="20"><use href="#phone"/></svg><span class="contact__phone">306-555-0147</span></div>
    <div class="contact__row" style="margin-top:2px"><svg width="20" height="20"><use href="#globe"/></svg><span class="contact__web">www.brellovanesk.com</span></div>
  </div>
</section>

<!-- BACK -->
<section class="postcard postcard--back">
  <svg class="art" width="730" height="486" viewBox="0 0 730 486">
    <defs>
      <linearGradient id="skyTri" x1="0" y1="0" x2="0" y2="1">
        <stop offset="0" stop-color="#cfe7fa"/>
        <stop offset="1" stop-color="#3a8fd6"/>
      </linearGradient>
      <linearGradient id="fireTri2" x1="0" y1="0" x2="0" y2="1">
        <stop offset="0" stop-color="#f7b51b"/>
        <stop offset="1" stop-color="#ee3a1f"/>
      </linearGradient>
      <linearGradient id="photoA" x1="0" y1="0" x2="1" y2="1">
        <stop offset="0" stop-color="#d9dde2"/>
        <stop offset=".5" stop-color="#b33a36"/>
        <stop offset="1" stop-color="#5d8a4a"/>
      </linearGradient>
      <linearGradient id="photoB" x1="0" y1="0" x2="1" y2="1">
        <stop offset="0" stop-color="#f2f2f2"/>
        <stop offset="1" stop-color="#a9b3be"/>
      </linearGradient>
    </defs>
    <polygon points="0,0 322,0 384,210 318,395 0,395" fill="var(--blue)"/>
    <polygon points="324,0 420,0 386,202" fill="url(#skyTri)"/>
    <polygon points="322,396 386,222 438,396" fill="url(#fireTri2)"/>
    <polygon role="img" aria-label="Photo of two technicians talking beside an outdoor air conditioning unit" points="0,288 188,282 160,380 0,384" fill="url(#photoA)" stroke="#fff" stroke-width="3"/>
    <polygon role="img" aria-label="Photo of gloved hands repairing pipes with a wrench" points="200,282 345,282 315,380 168,380" fill="url(#photoB)" stroke="#fff" stroke-width="3"/>
    <polygon points="0,398 440,398 468,486 0,486" fill="var(--grey)"/>
    <line x1="40" y1="66" x2="308" y2="66" stroke="#9cc4e8" stroke-width="1"/>
    <line x1="40" y1="66" x2="88" y2="66" stroke="var(--orange)" stroke-width="3.5" stroke-linecap="round"/>
    <g class="message-lines" stroke="var(--write-line)" stroke-width="1">
      <line x1="40" y1="104" x2="330" y2="104"/>
      <line x1="40" y1="136" x2="338" y2="136"/>
      <line x1="40" y1="168" x2="348" y2="168"/>
      <line x1="40" y1="200" x2="356" y2="200"/>
      <line x1="40" y1="232" x2="360" y2="232"/>
      <line x1="40" y1="262" x2="350" y2="262"/>
    </g>
    <rect x="640" y="40" width="58" height="56" fill="var(--stamp)"/>
    <g stroke="#b5b5b5" stroke-width="1">
      <line x1="428" y1="162" x2="692" y2="162"/>
      <line x1="428" y1="208" x2="692" y2="208"/>
      <line x1="428" y1="253" x2="692" y2="253"/>
      <line x1="428" y1="302" x2="692" y2="302"/>
    </g>
  </svg>

  <div class="abs note__title" style="left:40px;top:32px">A NOTE <span>FOR YOU</span></div>

  <div class="abs brand" style="left:430px;top:46px">
    <i class="brand__dot" style="width:10px;height:10px"></i><span class="brand__name" style="font-size:20px">BrelloVane</span>
  </div>
  <div class="abs brand__services" style="left:430px;top:76px;font-size:8px">Heating • Cooling • Electrical • Plumbing</div>

  <div class="abs contact" style="left:40px;top:406px">
    <div class="contact__row"><svg width="20" height="20"><use href="#phone"/></svg><span class="contact__phone">306-555-0147</span></div>
    <div class="contact__row" style="margin-top:2px"><svg width="20" height="20"><use href="#globe"/></svg><span class="contact__web">www.brellovanesk.com</span></div>
  </div>
  <div class="abs follow" style="left:364px;top:418px">follow us</div>
  <div class="abs social" style="left:366px;top:436px"><i></i><i></i></div>
</section>

</body>
</html>
```